willow crest business card project

Financial consulting in line with life insurance ,index annuity, college funding solutions. I educate clients on cash flow, debt management, how to create emergency fund, how to proper protection with the best insurance, how to accummulate asset and management, how to preserve asset/ estate planning. Collge funding solutions help familes seek the best funding solutions possible including award letter review and test prep on QEV, BRM, LBRM, BRM II
Target Market(s)
Individuals, family, business
Industry/Entity Type
Financial Planning
Contact Information for Business Card
Business name: Willow Crest Financial Services
Dorin Velko
Managing Director
License no. 5K32416
Address: 2193 Thistlebrook Ave. Baldwin Park, CA 91724
Phone: 714-555-0193 Fax: 626-555-0147
Email: dorin.velko@mailbrook.example
Other font styles liked:
- Bliss
Requirements
Must have
- Use feng shui as a guide to design the card make a flow curve lines only no angle or arrows.Size 3.5 inch by 2inch, metallic look is good, design a logo too . Keep it simple add image using feng shuis a guide. Also put a tagline that can make a very good impression. Use the back with something that the client we be able to use feng shui as guide.
Nice to have
- Use feng shui as guiding principle. Keep it simple
- Logo and tagline
Should not have
- Negative chi ,Angles, down ward design, too many things or too many images

```html
<!DOCTYPE html>
<html lang="en">
<head>
<meta charset="utf-8">
<title>Willow Crest Financial Services – Business Card</title>
<link rel="stylesheet" href="https://fonts.googleapis.com/css2?family=Open+Sans:wght@400;700&family=Questrial&display=swap">
<style>
  :root {
    --stage: #000000;
    --paper: #ffffff;
    --brand-red: #ed1c24;
    --brand-red-deep: #e3161e;
    --ink: #1e1e1e;
    --ink-soft: #3a3a3a;
    --font-brand: "Questrial", "Century Gothic", sans-serif;
    --font-body: "Open Sans", Arial, sans-serif;
  }
  html, body {
    margin: 0;
    padding: 0;
    width: 1200px;
    height: 900px;
    overflow: hidden;
    background: var(--stage);
  }
  .canvas {
    position: relative;
    width: 1200px;
    height: 900px;
    background: var(--stage);
  }
  .card {
    position: absolute;
    width: 477px;
    height: 293px;
    box-sizing: border-box;
  }
  .card--front {
    left: 116px;
    top: 275px;
    background: var(--paper);
    border-radius: 0 52px 0 52px;
  }
  .card--back {
    left: 622px;
    top: 276px;
    background: linear-gradient(120deg, var(--brand-red-deep) 0%, var(--brand-red) 45%, var(--brand-red) 100%);
    border-radius: 52px 0 52px 0;
  }

  /* Front: person */
  .person {
    position: absolute;
    right: 22px;
    top: 36px;
    text-align: right;
    font-family: var(--font-body);
  }
  .person__name {
    margin: 0;
    font-size: 17px;
    font-weight: 700;
    color: var(--ink);
    line-height: 22px;
  }
  .person__surname { color: var(--brand-red); }
  .person__title {
    margin: 0;
    font-size: 12.5px;
    color: var(--ink);
    line-height: 18px;
  }

  /* Brand wordmark */
  .brand {
    position: absolute;
    font-family: var(--font-brand);
    line-height: 1;
  }
  .brand__name {
    display: block;
    font-weight: 400;
    white-space: nowrap;
  }
  .brand__sub {
    display: block;
    letter-spacing: 0.3px;
    white-space: nowrap;
  }
  .brand--front { left: 31px; top: 90px; color: var(--ink); }
  .brand--front .brand__name { font-size: 47px; }
  .brand--front .brand__sub { font-size: 15px; margin: 4px 0 0 91px; color: var(--ink-soft); }
  .brand--back { right: 36px; top: 197px; color: var(--paper); text-align: right; }
  .brand--back .brand__name { font-size: 39px; }
  .brand--back .brand__sub { font-size: 13.5px; margin: 3px 56px 0 0; }

  /* Front: contacts */
  .contact {
    position: absolute;
    right: 22px;
    top: 159px;
    margin: 0;
    padding: 0;
    list-style: none;
    font-family: var(--font-body);
    font-size: 12.5px;
    color: var(--ink);
    text-align: right;
  }
  .contact__item {
    display: flex;
    justify-content: flex-end;
    align-items: center;
    gap: 5px;
    height: 20px;
  }
  .contact__icon { width: 10px; height: 10px; fill: var(--ink); }
  .address {
    position: absolute;
    right: 24px;
    top: 231px;
    margin: 0;
    font-family: var(--font-body);
    font-style: normal;
    font-size: 12.5px;
    line-height: 21px;
    color: var(--ink);
    text-align: right;
  }
</style>
</head>
<body>
<main class="canvas">
  <section class="card card--front" aria-label="Business card front">
    <div class="person">
      <p class="person__name">Dorin <span class="person__surname">Velko</span></p>
      <p class="person__title">Managing Director</p>
    </div>

    <div class="brand brand--front">
      <span class="brand__name">Willow Crest</span>
      <span class="brand__sub">FINANCIAL SERVICES</span>
    </div>

    <ul class="contact">
      <li class="contact__item">714-555-0193
        <svg class="contact__icon" viewBox="0 0 10 10" aria-hidden="true"><path d="M2.2 0.6l1.5 1.9-0.9 1.1c0.6 1.3 1.5 2.2 2.8 2.8l1.1-0.9 1.9 1.5-0.8 1.6C5.9 8.6 1.4 4.1 0.6 2.2z"/></svg>
      </li>
      <li class="contact__item">626-555-0147
        <svg class="contact__icon" viewBox="0 0 10 10" aria-hidden="true"><path d="M3 0.5h4v2.5H3z M1 3.5h8v6H1z" fill-rule="evenodd"/><rect x="3" y="5" width="4" height="0.9" fill="#fff"/><rect x="3" y="7" width="4" height="0.9" fill="#fff"/></svg>
      </li>
      <li class="contact__item">dorin.velko@mailbrook.example
        <svg class="contact__icon" viewBox="0 0 10 10" aria-hidden="true"><path d="M0.5 2h9v6.5h-9z"/><path d="M0.8 2.3L5 5.6 9.2 2.3" stroke="#fff" stroke-width="0.9" fill="none"/></svg>
      </li>
    </ul>

    <address class="address">2193 Thistlebrook Ave<br>Baldwin Park, CA 91724</address>
  </section>

  <section class="card card--back" aria-label="Business card back">
    <div class="brand brand--back">
      <span class="brand__name">Willow Crest</span>
      <span class="brand__sub">FINANCIAL SERVICES</span>
    </div>
  </section>
</main>
</body>
</html>
```